BrewDune Lane.

I want the full logo on one side. And the other side the card if right Ralf the logo the left half orange like the car in the logo color with Lorena J Torvand
Founder and CEO
Email symbol then ltorvand@brewdunelanex.com
Www symbol. Then Brewdunelanex.com
Phone symbol then 555-214-BREW
The very bottom would like Brew Dune Lane is a division of Tumbler Treks. LLC

```html
<!DOCTYPE html>
<html lang="en">
<head>
<meta charset="utf-8">
<title>Brew Dune Lane – Business Card</title>
<link href="https://fonts.googleapis.com/css2?family=Work+Sans:wght@400;500&display=swap" rel="stylesheet">
<style>
  :root{
    --stage:#1c1c1c;
    --card-dark:#262626;
    --card-light:#ffffff;
    --orange:#e98f25;
    --ink:#1a1a1a;
    --cream:#f3e7d3;
    --teal:#8fd1c4;
  }
  *{margin:0;padding:0;box-sizing:border-box}
  html,body{width:1200px;height:900px;overflow:hidden}
  body{background:var(--stage);font-family:"Work Sans",Arial,sans-serif;position:relative}
  .card{position:absolute;left:290px;width:620px;height:354px;overflow:hidden}
  .card--back{top:60px;background:var(--card-dark)}
  .card--front{top:486px;background:var(--card-light)}

  .logo-art{position:absolute;border-radius:4px;
    background:linear-gradient(180deg,var(--teal) 0%,var(--orange) 45%,#c9721c 80%,var(--cream) 100%)}
  .brand-name{position:absolute;font-weight:500;letter-spacing:1px;white-space:nowrap;text-align:center}

  .card--back .logo-art{left:230px;top:70px;width:160px;height:70px}
  .card--back .brand-name{left:0;width:620px;top:152px;font-size:40px;color:#fff}
  .card--back .site{position:absolute;left:0;width:620px;top:282px;text-align:center;
    color:#fff;font-size:15px;letter-spacing:.5px}
  .accent{color:var(--orange)}

  .card--front .logo-art{left:412px;top:56px;width:136px;height:62px}
  .card--front .brand-name{left:350px;width:260px;top:126px;font-size:26px;color:var(--ink)}
  .person{position:absolute;left:40px;top:112px}
  .person__name{color:var(--orange);font-size:21px;font-weight:500;letter-spacing:1.5px;text-transform:uppercase}
  .person__role{color:var(--ink);font-size:15px;margin-top:2px}
  .divider{position:absolute;left:40px;top:180px;width:540px;height:1.5px;background:var(--orange)}
  .contacts{position:absolute;left:30px;top:196px;list-style:none}
  .contacts li{display:flex;align-items:center;gap:8px;font-size:16px;color:var(--ink);height:25px}
  .contacts svg{width:12px;height:12px;flex:none}
  .address{position:absolute;right:40px;top:200px;text-align:right;font-size:16px;color:var(--ink);line-height:1.45;font-style:normal}
  .wave{position:absolute;left:0;top:0;width:620px;height:354px}
  .division{position:absolute;left:0;width:620px;top:332px;text-align:center;font-size:11px;color:#fff;letter-spacing:.3px}
</style>
</head>
<body>
  <section class="card card--back">
    <div class="logo-art" role="img" aria-label="Illustration of an orange station wagon with bottles, surfboard and beach fence"></div>
    <div class="brand-name">Brew Dune Lane</div>
    <p class="site">www.<span class="accent">Brewdunelanex</span>.com</p>
  </section>

  <section class="card card--front">
    <svg class="wave" viewBox="0 0 620 354" aria-hidden="true">
      <path d="M0 290 C100 312 220 326 360 322 C480 318 560 306 620 296 L620 354 L0 354Z" fill="var(--orange)"/>
      <path d="M0 284 C100 306 220 320 360 316 C480 312 560 300 620 290" fill="none" stroke="var(--ink)" stroke-width="4"/>
    </svg>

    <div class="person">
      <div class="person__name">Lorena J Torvand</div>
      <div class="person__role">Founder and CEO</div>
    </div>
    <div class="divider"></div>

    <ul class="contacts">
      <li><svg viewBox="0 0 12 12"><path d="M3 1 L5 3.5 L4 5 Q5 7.5 7 8 L8.5 7 L11 9 L10 11 Q4 11 1 3 Z" fill="var(--orange)"/></svg><span>555-214-BREW</span></li>
      <li><svg viewBox="0 0 12 12"><rect x="1" y="2.5" width="10" height="7" fill="none" stroke="var(--orange)" stroke-width="1.2"/><path d="M1 3 L6 7 L11 3" fill="none" stroke="var(--orange)" stroke-width="1.2"/></svg><span>ltorvand@brewdunelanex.com</span></li>
      <li><svg viewBox="0 0 12 12"><circle cx="6" cy="6" r="5" fill="none" stroke="var(--orange)" stroke-width="1.2"/><ellipse cx="6" cy="6" rx="2.2" ry="5" fill="none" stroke="var(--orange)" stroke-width="1"/><path d="M1 6 H11" stroke="var(--orange)" stroke-width="1"/></svg><span>www.<span class="accent">Brewdunelanex</span>.com</span></li>
    </ul>

    <div class="logo-art" role="img" aria-label="Illustration of an orange station wagon with bottles, surfboard and beach fence"></div>
    <div class="brand-name">Brew Dune Lane</div>

    <address class="address">214b Harbour Row,<br>Port Lindel, NZ, 8042</address>

    <p class="division">Brew Dune Lane is a division of Tumbler Treks. LLC</p>
  </section>
</body>
</html>
```